K7 Teardown looking for leading edge design not typical for our industry

We need to incorporate our new company tag line "foundations, follow-through, fairness" into our cards. Im open to any type of design for this and colour treatment. In fact the whole card needs a new lay out including the back. "Sustainable Deconstruction" needs to be removed from the back and the new tagline used. Would like to see different text and treatment used for "Deconstruction & Demolition".

Target Market(s)

Construction

Industry/Entity Type

Construction Company

Contact Information for Business Card

Standard business card size

Font styles to use
Sans Serif

Colors
9bcb3c
0255a3
f37122

Requirements
Should not have
• Irregular sizing.

```html
<!DOCTYPE html>
<html lang="en">
<head>
<meta charset="utf-8">
<title>K7 Teardown — Business Card</title>
<link href="https://fonts.googleapis.com/css2?family=Arimo:wght@400;700&display=swap" rel="stylesheet">
<style>
  :root {
    --bg: #2d2d2d;
    --card: #2a2a2a;
    --card-edge: #1c1c1c;
    --band: #e4e4e4;
    --blue: #0255a3;
    --blue-light: #3a86d1;
    --green: #9bcb3c;
    --orange: #f37122;
    --white: #f2f2f2;
    --muted: #cfcfcf;
  }
  * { box-sizing: border-box; margin: 0; padding: 0; }
  html, body { width: 1200px; height: 903px; overflow: hidden; }
  body {
    background: var(--bg);
    font-family: "Arimo", Arial, sans-serif;
    display: flex;
    align-items: center;
    justify-content: center;
    gap: 40px;
  }
  .card {
    position: relative;
    width: 540px;
    height: 309px;
    background: var(--card);
    border-radius: 3px;
    box-shadow: 0 6px 0 var(--card-edge), 0 14px 28px rgba(0,0,0,.45);
    overflow: hidden;
  }

  /* Front */
  .card-front .top-band {
    position: absolute; left: 0; top: 0; right: 0; height: 96px;
    background: var(--band);
    border-bottom: 4px solid var(--orange);
  }
  .front-tagline {
    position: absolute; right: 22px; top: 18px;
    color: var(--blue);
    font-size: 11px;
    letter-spacing: 1px;
    text-transform: uppercase;
  }
  .brand-mark {
    position: absolute; left: 30px; top: 26px;
    width: 100px; height: 100px; border-radius: 50%;
    background: var(--white);
    border: 8px solid var(--blue);
  }
  .brand-name {
    position: absolute; left: 146px; top: 104px;
    color: var(--blue-light);
    font-size: 24px;
    font-weight: 700;
    letter-spacing: 1px;
    text-transform: uppercase;
  }
  .brand-sub {
    position: absolute; left: 146px; top: 134px;
    color: var(--green);
    font-size: 12px;
    font-weight: 400;
    letter-spacing: 3px;
    text-transform: uppercase;
  }
  .person {
    position: absolute; left: 30px; bottom: 28px;
    color: var(--white);
  }
  .person-name { font-size: 24px; font-weight: 400; }
  .person-title { font-size: 14px; color: var(--orange); margin-top: 3px; }
  .contact {
    position: absolute; right: 22px; top: 156px;
    list-style: none;
    color: var(--muted);
    font-size: 11px;
    line-height: 15px;
    text-align: right;
  }
  .contact li { display: flex; justify-content: flex-end; align-items: center; gap: 8px; }
  .contact .icon {
    width: 8px; height: 8px; background: var(--green);
    border-radius: 50%; flex: none;
  }
  .address {
    position: absolute; right: 22px; bottom: 28px;
    color: var(--muted); font-size: 11px;
  }

  /* Back */
  .card-back .back-lockup {
    position: absolute; left: 50%; top: 50%;
    transform: translate(-50%, -58%);
    display: flex; align-items: center; gap: 20px;
  }
  .back-ring {
    flex: none;
    width: 90px; height: 90px; border-radius: 50%;
    border: 12px solid var(--green);
  }
  .back-name {
    color: var(--blue-light);
    font-size: 34px;
    font-weight: 700;
    letter-spacing: 1px;
    text-transform: uppercase;
    white-space: nowrap;
  }
  .back-tagline {
    position: absolute; left: 0; right: 0; bottom: 70px;
    text-align: center;
    color: var(--orange);
    font-size: 13px;
    letter-spacing: 2px;
    text-transform: uppercase;
  }
  .back-rule {
    position: absolute; left: 0; right: 0; bottom: 0; height: 6px;
    background: var(--blue);
  }
</style>
</head>
<body>
  <section class="card card-front" aria-label="Business card front">
    <div class="top-band"></div>
    <div class="front-tagline">foundations, follow-through, fairness</div>
    <div class="brand-mark"></div>
    <div class="brand-name">K7 Teardown</div>
    <div class="brand-sub">Deconstruction &amp; Demolition Inc.</div>

    <ul class="contact">
      <li>(555) 201 4470 <span class="icon"></span></li>
      <li>(555) 318 9024 <span class="icon"></span></li>
      <li>(555) 201 4471 <span class="icon"></span></li>
      <li>www.k7teardown.com <span class="icon"></span></li>
      <li>marcus@k7teardown.com <span class="icon"></span></li>
    </ul>

    <div class="person">
      <div class="person-name">Marcus Hale</div>
      <div class="person-title">Head Estimater</div>
    </div>
    <div class="address">#200, 4410-97 Street Riverton, AB T0X 1A0</div>
  </section>

  <section class="card card-back" aria-label="Business card back">
    <div class="back-lockup">
      <div class="back-ring"></div>
      <div class="back-name">K7 Teardown</div>
    </div>
    <div class="back-tagline">foundations, follow-through, fairness</div>
    <div class="back-rule"></div>
  </section>
</body>
</html>
```